<希望の方向性>--------
パッケージデザインの最終目標は「高品質・効果への期待感」を感じてもらうことです。
なおかつ、数ある健康食品の中で、印象に残るパッケージデザインを希望いたします。
【デザインに求めるもの】
●高級感 ●高品質感 ●毒素排泄 ●健康(1つランク上の健康)
というのが明瞭なこと。

●幅広い世代に受け入れやすいデザイン。

【希望のカラー】
●メインカラー:黄色 ポイントに赤を使用
健康・元気を演出したいので、黄色を中心としたデザインでお願いします。
【容器仕様】
●化粧箱
●印刷は2C希望ですが、3Cでも可。

サイズは添付にて詳細ご確認ください。

【表面記載内容】
●商品名 [OKU ドレファ] を入れる。
※OKUに関しては大文字
※OKUは弊社のロゴや現在のデザインを使わない
※「QBRTマーク」「健康補助食品」は記載しなくて構いません。(他に入れる文字はありません)

幅広い世代にわかりやすいワードと想定しています。
■ その他/注意点
選択させて頂いたパッケージデザインの著作権(財産権)等の扱いはTorvia利用規約に従い、弊社に譲渡をお願いします。フォントや画像素材などを利用する場合は上記利用用途に使用できることを確認し、第三者の知的財産権等に注意して下さい。
皆様大変素敵なデザインを本当にありがとうございます。
今週、社内で当選作品を検討いたします。
来週の月曜日に当選作品を決定・発表いたします。

何卒よろしくお願いいたします。

素敵なデザインを本当にありがとうございました。

社長の希望通りのデザインで大変満足されていました。
インパクトがあり、高品質を期待できるパッケージデザインだったので選ばせて頂きました。

トルヴィアの皆様、素晴らしいデザインの提案誠にありがとうございました。
たくさんの素敵な提案を頂き選考がとても大変という、嬉しい悩みもありましたが、満足のいく作品を選ぶことができ、本当に喜んでおります。
全てトルヴィアの皆様のおかげでございます。
本当にありがとうございました。

```html
<!DOCTYPE html>
<html lang="ja">
<head>
<meta charset="UTF-8">
<title>OKU ドレファ パッケージ</title>
<link rel="stylesheet" href="https://fonts.googleapis.com/css2?family=Noto+Sans+JP:wght@300;400;500&display=swap">
<style>
  :root {
    --bg-yellow: #d8ee2a;
    --structure-tone: #cfe528;
    --ink-white: #ffffff;
  }
  html, body {
    margin: 0;
    padding: 0;
    width: 825px;
    height: 1200px;
    overflow: hidden;
  }
  .package-front {
    position: relative;
    width: 825px;
    height: 1200px;
    background: var(--bg-yellow);
    font-family: "Noto Sans JP", sans-serif;
    color: var(--ink-white);
    overflow: hidden;
  }
  .molecule-diagram {
    position: absolute;
    left: 205px;
    top: 150px;
    width: 415px;
    height: 305px;
    background: var(--structure-tone);
    border-radius: 6px;
  }
  .title-rule {
    position: absolute;
    left: 96px;
    width: 633px;
    height: 11px;
    background: var(--ink-white);
  }
  .title-rule.top { top: 490px; }
  .title-rule.bottom { top: 688px; }
  .product-name {
    position: absolute;
    left: 96px;
    width: 633px;
    top: 530px;
    margin: 0;
    text-align: center;
    font-weight: 400;
    font-size: 90px;
    line-height: 130px;
    letter-spacing: 6px;
    white-space: nowrap;
  }
  .product-name .gap { letter-spacing: 0; margin-right: -8px; }
  .product-info {
    position: absolute;
    left: 96px;
    top: 738px;
    width: 640px;
    font-size: 16px;
    line-height: 29px;
    font-weight: 400;
  }
  .product-info p { margin: 0; }
  .product-info .category { margin-bottom: 8px; }
</style>
</head>
<body>
  <main class="package-front">
    <div class="molecule-diagram" role="img" aria-label="N-アセチルグルコサミンの化学構造式（白い線画）"></div>

    <div class="title-rule top"></div>
    <h1 class="product-name">OKU<span class="gap"> </span>ドレファ</h1>
    <div class="title-rule bottom"></div>

    <section class="product-info">
      <p class="category">■健康補助食品</p>
      <p>本製品は N-アセチルグルコサミンを主な原材料としています。</p>
      <p>ドレファとは N-アセチルグルコサミンの略称です。</p>
    </section>
  </main>
</body>
</html>
```